Flyer Design Project

Painting and Maintenance
This is what I have as idea as Job description
Refresh, renew & revive your home. from painting to carpentry. Do you guys have any epic unique slogan?
As what we do Residential - Commercial Interior - ExteriorTrim & Molding installationWainscoting - Wallpaper removalCabinet refinishing Woodwork EnamelingDeck & Fence Cleaning & SealingPressure washConcrete & Paver Washing
I would like to have a note that says-Prompt professional service-Free estimates-Insured -"visit us on PalPorch"
I would like new ideas from you guys as well!
Carpentry

```html
<!DOCTYPE html>
<html lang="en">
<head>
<meta charset="utf-8">
<title>Harwell Painting &amp; Maintenance – Flyers</title>
<link href="https://fonts.googleapis.com/css2?family=Oswald:wght@400;500;700&family=Open+Sans:wght@400;600&display=swap" rel="stylesheet">
<style>
:root{
  --page:#ffffff;
  --cream:#fbf6e8;
  --maroon:#5e3340;
  --maroon-dark:#4a2631;
  --red:#c8202f;
  --brand-red:#b3212c;
  --pink:#e23a5c;
  --ink:#3a2328;
  --white:#ffffff;
  --warm-1:#f3d7a8;
  --warm-2:#e9b77a;
  --cool-1:#efe6d6;
  --cool-2:#c9b8a0;
}
*{box-sizing:border-box;margin:0;padding:0}
html,body{width:1200px;height:424px;overflow:hidden;background:var(--page)}
body{position:relative;font-family:"Open Sans",sans-serif}
.flyer{position:absolute;top:28px;width:557px;height:364px;background:var(--cream);overflow:hidden}
.flyer--front{left:38px}
.flyer--back{left:607px}
.room-photo{position:absolute;top:0;height:310px}
.flyer--front .room-photo{left:190px;right:0;background:radial-gradient(ellipse at 70% 25%,#fff6e0 0%,var(--warm-1) 35%,var(--warm-2) 100%);
  -webkit-mask-image:linear-gradient(90deg,transparent 0,#000 70px);mask-image:linear-gradient(90deg,transparent 0,#000 70px)}
.flyer--back .room-photo{left:0;right:190px;background:radial-gradient(ellipse at 55% 60%,#fbf7ef 0%,var(--cool-1) 40%,var(--cool-2) 100%);
  -webkit-mask-image:linear-gradient(270deg,transparent 0,#000 70px);mask-image:linear-gradient(270deg,transparent 0,#000 70px)}
.paint-roller{position:absolute;width:190px;height:290px;bottom:30px;
  background:linear-gradient(160deg,#f06a80 0%,var(--pink) 45%,#b81d3c 100%);border-radius:10px}
.flyer--front .paint-roller{left:0}
.flyer--back .paint-roller{right:0}
.footer-band{position:absolute;left:0;bottom:0;width:557px;height:80px}
.footer-text{position:absolute;left:0;right:0;bottom:26px;text-align:center;color:var(--white);
  font-family:"Open Sans",sans-serif;font-size:12.5px;letter-spacing:2.2px;word-spacing:2px}
.footer-text .sep{opacity:.7;margin:0 9px}
.brand{position:absolute;top:26px;width:150px;text-align:center;color:var(--brand-red);font-family:"Oswald",sans-serif;font-weight:700;line-height:.95}
.brand__name{display:block;font-size:27px;letter-spacing:.5px}
.brand__sub{display:block;font-size:11px;letter-spacing:.6px;margin-top:3px}
.flyer--front .brand{left:18px}
.flyer--back .brand{right:18px}
.headline{position:absolute;left:262px;top:44px;width:280px;color:var(--maroon);font-family:"Oswald",sans-serif;text-align:center}
.headline__lead{display:block;font-size:22px;font-weight:700;letter-spacing:1px;color:var(--brand-red)}
.headline__main{display:block;font-size:54px;font-weight:700;line-height:1;letter-spacing:1px;color:var(--maroon)}
.headline__tag{display:block;font-size:19px;font-weight:400;letter-spacing:1px;margin-top:14px}
.social-pill{position:absolute;top:260px;height:36px;display:flex;align-items:center;border-radius:18px;
  background:var(--white);border:2px solid var(--maroon);overflow:hidden;box-shadow:0 1px 3px rgba(0,0,0,.25)}
.flyer--front .social-pill{left:294px}
.flyer--back .social-pill{left:76px}
.social-pill__label{padding:0 12px 0 14px;font-family:"Oswald",sans-serif;font-weight:500;font-size:17px;color:var(--maroon);letter-spacing:1px}
.social-pill__name{height:100%;display:flex;align-items:center;padding:0 18px 0 12px;background:var(--maroon);
  color:var(--white);font-family:"Open Sans",sans-serif;font-weight:600;font-size:19px}
.services{position:absolute;left:32px;top:26px;list-style:none}
.services li{display:flex;align-items:center;height:14.7px;font-size:10.5px;color:var(--ink)}
.services li::before{content:"";width:14px;height:5px;border-radius:2px;background:var(--maroon);margin-right:9px;box-shadow:-3px 0 0 var(--brand-red)}
</style>
</head>
<body>

<section class="flyer flyer--front">
  <div class="room-photo" role="img" aria-label="Warmly lit living room with sofa and window"></div>
  <div class="paint-roller" role="img" aria-label="Hand holding a red paint roller"></div>
  <div class="brand"><span class="brand__name">HARWELL<br>PAINTING</span><span class="brand__sub">&amp; MAINTENANCE LLC.</span></div>
  <h1 class="headline">
    <span class="headline__lead">GIVE YOUR HOME A</span>
    <span class="headline__main">FACELIFT</span>
    <span class="headline__tag">REFRESH • RENEW • REVIVE</span>
  </h1>
  <svg class="footer-band" viewBox="0 0 557 80" aria-hidden="true"><path d="M0 22 Q280 -8 557 14 L557 80 L0 80 Z" fill="var(--maroon)"/></svg>
  <div class="social-pill"><span class="social-pill__label">VISIT US ON</span><span class="social-pill__name">PalPorch</span></div>
  <p class="footer-text">PROMPT PROFESSIONAL SERVICE<span class="sep">|</span>FREE ESTIMATES<span class="sep">|</span>INSURED</p>
</section>

<section class="flyer flyer--back">
  <div class="room-photo" role="img" aria-label="Bright modern living room interior"></div>
  <div class="paint-roller" role="img" aria-label="Hand holding a red paint roller"></div>
  <ul class="services">
    <li>Residential - Commercial</li>
    <li>Interior - Exterior</li>
    <li>Trim &amp; Molding Installation</li>
    <li>Wainscoting</li>
    <li>Wallpaper removal</li>
    <li>Cabinet refinishing</li>
    <li>Woodwork Enameling</li>
    <li>Deck &amp; Fence Cleaning &amp; Sealing</li>
    <li>Pressure wash</li>
    <li>Concrete &amp; Paver Washing</li>
  </ul>
  <div class="brand"><span class="brand__name">HARWELL<br>PAINTING</span><span class="brand__sub">&amp; MAINTENANCE LLC.</span></div>
  <svg class="footer-band" viewBox="0 0 557 80" aria-hidden="true"><path d="M0 14 Q277 -8 557 22 L557 80 L0 80 Z" fill="var(--maroon)"/></svg>
  <div class="social-pill"><span class="social-pill__label">VISIT US ON</span><span class="social-pill__name">PalPorch</span></div>
  <p class="footer-text">PROMPT PROFESSIONAL SERVICE<span class="sep">|</span>FREE ESTIMATES<span class="sep">|</span>INSURED</p>
</section>

</body>
</html>
```